yard sign for lawncare business

I need a lawn sign design. ...The sign will be 18"X27"....it will be displayed with the 27" running horizontally. ...i need the company name and logo to be included and the same color as the graphic in the included file.....i also want the slogan included as well as the phone number 256-555-0148...all wording and numbers should be large and easy to see from passing cars on the road.....feel free to play around with background colors and wording and number placement
Updates

Ok guys....downloads are now available for viewing. ..sorry about the delay....thanks for your help and good luck

Industry/Entity Type

Business

```html
<!DOCTYPE html>
<html lang="en">
<head>
<meta charset="utf-8">
<title>Mowcrest Yard Sign</title>
<link rel="stylesheet" href="https://fonts.googleapis.com/css2?family=Roboto+Condensed:wght@700;900&display=swap">
<style>
  :root {
    --page-bg: #eef0ec;
    --sky-top: #29a8e6;
    --sky-mid: #8fd3f5;
    --sky-low: #e9f7fd;
    --leaf-green: #7cbd34;
    --leaf-deep: #4e9a1c;
    --band-green: #7ab838;
    --slate-grey: #878787;
    --white: #ffffff;
  }
  * { margin: 0; padding: 0; box-sizing: border-box; }
  html, body {
    width: 1200px;
    height: 1000px;
    overflow: hidden;
    background: var(--page-bg);
  }
  .yard-sign {
    position: absolute;
    left: 50px;
    top: 135px;
    width: 1100px;
    height: 729px;
    box-shadow: 0 8px 24px rgba(0, 0, 0, 0.18);
  }
  .yard-sign svg { display: block; width: 100%; height: 100%; }
  .brand-name {
    font-family: "Roboto Condensed", "Arial Narrow", sans-serif;
    font-weight: 900;
    fill: var(--leaf-green);
  }
  .slogan {
    font-family: "Roboto Condensed", "Arial Narrow", sans-serif;
    font-weight: 700;
    fill: var(--white);
  }
  .phone-number {
    font-family: "Roboto Condensed", "Arial Narrow", sans-serif;
    font-weight: 700;
    fill: var(--slate-grey);
  }
  .sky-stop-top { stop-color: var(--sky-top); }
  .sky-stop-mid { stop-color: var(--sky-mid); }
  .sky-stop-low { stop-color: var(--sky-low); }
  .turf-stop-clear { stop-color: var(--leaf-green); stop-opacity: 0; }
  .turf-stop-soft { stop-color: var(--leaf-green); stop-opacity: 0.55; }
  .turf-stop-deep { stop-color: var(--leaf-deep); stop-opacity: 0.9; }
  .slogan-band { fill: var(--band-green); }
</style>
</head>
<body>
  <div class="yard-sign">
    <svg viewBox="0 0 800 530" xmlns="http://www.w3.org/2000/svg">
      <defs>
        <linearGradient id="sky-fill" x1="0" y1="0" x2="0" y2="1">
          <stop offset="0" class="sky-stop-top"/>
          <stop offset="0.45" class="sky-stop-mid"/>
          <stop offset="1" class="sky-stop-low"/>
        </linearGradient>
        <linearGradient id="turf-fill" x1="0" y1="0" x2="0" y2="1">
          <stop offset="0" class="turf-stop-clear"/>
          <stop offset="0.5" class="turf-stop-soft"/>
          <stop offset="1" class="turf-stop-deep"/>
        </linearGradient>
      </defs>

      <rect class="sign-sky" x="0" y="0" width="800" height="530" fill="url(#sky-fill)"/>

      <text class="brand-name" x="45" y="325" font-size="126" textLength="700" lengthAdjust="spacingAndGlyphs">MOWCREST</text>

      <rect class="slogan-band" x="0" y="348" width="800" height="52"/>
      <text class="slogan" x="60" y="385" font-size="30" textLength="680" lengthAdjust="spacingAndGlyphs">WHEN YOUR GRASS GETS TALL, GIVE US A CALL.</text>

      <rect class="turf-strip" role="img" aria-label="Illustrated strip of green grass blades along the bottom edge" x="0" y="440" width="800" height="90" fill="url(#turf-fill)"/>

      <text class="phone-number" x="142" y="497" font-size="86" textLength="512" lengthAdjust="spacingAndGlyphs">(256) 555-0148</text>
    </svg>
  </div>
</body>
</html>
```